Looking for a hot sauce label designed
Name: Copper Lantern Hot sauce
Graphic: dragon in pictures supplied and the flame bigger going out in front of the dragon or happy for you to design a dragon in a similar style
Text font: using the text supplied for the name of the product only
Colour: Black graphic and text on light brown paper
Style: sketch dragon and text - simple minimalistic design
Label size: 7cm height x 17cm width

Target Market(s)

To sell in bars and supermarkets

Font styles to use
Script

Colors

Designer to choose only greyscale colors for use in the design.

Requirements
Must have
• Name of product: Copper Lantern Hot Sauce
Batch No:
Business name and address
Best before date:
Nutrition Information Panel
Ingredients
Shake well before use
Keep refrigerated after opening
Australian made using 100% local ingredients
175ml
Room for a barcode
Nice to have
• Any changes you think will improve label design

```html
<!DOCTYPE html>
<html lang="en">
<head>
<meta charset="utf-8">
<title>Copper Lantern Hot Sauce – Label</title>
<link href="https://fonts.googleapis.com/css2?family=Arimo:wght@400;700&family=Bangers&family=Oswald:wght@400;500;600&display=swap" rel="stylesheet">
<style>
  :root {
    --page-bg: #ffffff;
    --paper-top: #dcc6a3;
    --paper-bottom: #c9ab83;
    --ink: #141210;
    --ink-soft: #2b2723;
    --grey-mid: #6d6760;
    --grey-light: #a29b92;
    --faint-art: rgba(60, 50, 40, 0.14);
    --barcode-bg: #f4efe6;
  }
  * { box-sizing: border-box; margin: 0; padding: 0; }
  html, body {
    width: 1200px; height: 1200px; overflow: hidden;
    background: var(--page-bg);
  }
  .canvas { position: relative; width: 1200px; height: 1200px; }

  .label {
    position: absolute; left: 215px; top: 395px;
    width: 770px; height: 409px;
    background: linear-gradient(180deg, var(--paper-top) 0%, var(--paper-bottom) 100%);
    overflow: hidden;
    font-family: "Arimo", Arial, sans-serif;
    color: var(--ink);
  }

  .background-art {
    position: absolute; left: 0; top: 40px; width: 330px; height: 340px;
    border-radius: 45% 55% 40% 50%;
    background: radial-gradient(circle at 45% 45%, var(--faint-art) 0%, rgba(60,50,40,0) 70%);
  }

  .nutrition-panel {
    position: absolute; left: 49px; top: 26px; width: 219px; height: 195px;
    border: 1px solid var(--ink);
    padding: 8px 7px 6px;
    font-size: 9.5px; line-height: 1.2;
  }
  .nutrition-panel h2 {
    font-size: 14.5px; font-weight: 400; letter-spacing: 0.2px;
    margin-bottom: 5px;
  }
  .nutrition-panel .serving { display: flex; justify-content: space-between; font-weight: 700; }
  .nutrition-panel .serving span:last-child { width: 52px; }
  .nutrition-panel hr { border: 0; border-top: 1px solid var(--ink); margin: 4px -7px 5px; }
  .nutrition-table { width: 100%; border-collapse: collapse; font-weight: 700; }
  .nutrition-table th { text-align: left; font-weight: 700; vertical-align: top; padding-bottom: 12px; }
  .nutrition-table td { padding: 0; }
  .nutrition-table .col-serve { width: 78px; }
  .nutrition-table .col-100 { width: 52px; }

  .caution {
    position: absolute; left: 49px; top: 228px; width: 230px;
    font-size: 9.5px; line-height: 1.25; font-weight: 700;
  }
  .caution h3 { font-size: 14.5px; font-weight: 400; margin-bottom: 2px; }

  .ingredients {
    position: absolute; left: 49px; top: 278px; width: 225px;
    font-size: 9.5px; line-height: 1.3; font-weight: 700;
  }

  .storage {
    position: absolute; left: 49px; top: 320px; width: 225px;
    font-size: 9px; line-height: 1.25; font-weight: 700;
  }

  .brand-mini {
    position: absolute; left: 49px; top: 345px;
    font-family: "Oswald", "Arial Narrow", sans-serif;
    font-weight: 600; font-size: 19px; line-height: 1.2;
    text-transform: uppercase; color: var(--ink); letter-spacing: 0.5px;
  }
  .business-address {
    position: absolute; left: 49px; top: 372px; width: 225px;
    font-size: 8.5px; line-height: 1.25; color: var(--ink-soft);
  }

  .barcode-space {
    position: absolute; left: 292px; top: 262px; width: 56px; height: 124px;
    background: var(--barcode-bg);
    border: 1px solid var(--grey-mid);
  }

  .brand-name {
    position: absolute; left: 372px; top: 22px; width: 250px;
    font-family: "Oswald", "Arial Narrow", sans-serif;
    font-weight: 600; font-size: 52px; line-height: 1.05;
    color: var(--ink); text-align: center; text-transform: uppercase;
    letter-spacing: 1px;
  }

  .mascot-art {
    position: absolute; left: 361px; top: 150px; width: 292px; height: 176px;
    border-radius: 40% 45% 30% 35%;
    background: radial-gradient(ellipse at 40% 55%, var(--grey-light) 0%, var(--grey-mid) 45%, rgba(109,103,96,0) 72%);
  }

  .volume {
    position: absolute; left: 382px; top: 326px;
    font-family: "Oswald", "Arial Narrow", sans-serif;
    font-size: 12px; color: var(--ink-soft); letter-spacing: 0.5px;
  }
  .product-type {
    position: absolute; left: 380px; top: 340px;
    font-family: "Bangers", "Impact", sans-serif;
    font-size: 50px; line-height: 1; color: var(--ink);
    letter-spacing: 0.5px;
  }

  .origin-note {
    position: absolute; left: 714px; top: 32px;
    writing-mode: vertical-rl;
    font-family: "Oswald", "Arial Narrow", sans-serif;
    font-size: 12px; line-height: 1.25; font-weight: 500;
    text-transform: uppercase; color: var(--ink);
  }

  .batch-box {
    position: absolute; left: 706px; top: 193px; width: 52px; height: 196px;
    border: 1.5px solid var(--ink);
  }
  .batch-box .field-label {
    position: absolute; bottom: 8px;
    writing-mode: vertical-rl; transform: rotate(180deg);
    font-family: "Oswald", "Arial Narrow", sans-serif;
    font-size: 10px; color: var(--ink); letter-spacing: 0.4px;
  }
  .batch-box .field-line {
    position: absolute; top: 10px; width: 1px; height: 92px;
    background: var(--ink);
  }
  .batch-box .batch-label { left: 6px; }
  .batch-box .batch-line { left: 13px; }
  .batch-box .best-label { left: 27px; }
  .batch-box .best-line { left: 34px; height: 78px; }
</style>
</head>
<body>
<main class="canvas">
  <section class="label" aria-label="Copper Lantern Hot Sauce label">
    <div class="background-art" role="img" aria-label="Faint large dragon character sketch in the background"></div>

    <div class="nutrition-panel">
      <h2>NUTRITION INFORMATION</h2>
      <div class="serving"><span>Servings per package:</span><span>17.00</span></div>
      <div class="serving"><span>Serving size:</span><span>170.00mg</span></div>
      <hr>
      <table class="nutrition-table">
        <tr><th></th><th class="col-serve">Ave per<br>serve</th><th class="col-100">Ave per<br>100ml</th></tr>
        <tr><td>Energy</td><td>257g</td><td>151 KJ</td></tr>
        <tr><td>Protein</td><td>1.5g</td><td>0.9g</td></tr>
        <tr><td>Fat, Total</td><td>3.2g</td><td>1.9g</td></tr>
        <tr><td>-saturated</td><td>0.5g</td><td>0.3g</td></tr>
        <tr><td>Carbohydrate</td><td>4.3g</td><td>2.5g</td></tr>
        <tr><td>-sugars</td><td>3.7g</td><td>2.2g</td></tr>
        <tr><td>Sodium</td><td>262g</td><td>154mg</td></tr>
      </table>
    </div>

    <div class="caution">
      <h3>CAUTION:</h3>
      <p>- Keep out of reach of children</p>
      <p>- Keep away and out of eyes</p>
    </div>

    <p class="ingredients">INGREDIENTS: Carrots, onion, habanero, water, lime juice, garlic, white vinegar, vegetable oil, ginger, cillantro, salt, pepper.</p>

    <div class="storage">
      <p>Shake well before use.</p>
      <p>Keep refrigerated after opening.</p>
    </div>

    <p class="brand-mini">Copper Lantern</p>
    <p class="business-address">Copper Lantern Foods<br>14 Ridgeway Lane, Ballarat VIC 3350</p>

    <div class="barcode-space" aria-label="Space reserved for barcode"></div>

    <h1 class="brand-name">Copper<br>Lantern</h1>

    <div class="mascot-art" role="img" aria-label="Sketched dragon character breathing a flame"></div>

    <p class="volume">175 ML</p>
    <p class="product-type">hot sauce</p>

    <p class="origin-note">Made using 100% fresh<br>Australian produce</p>

    <div class="batch-box">
      <span class="field-line batch-line"></span>
      <span class="field-label batch-label">BATCH N°</span>
      <span class="field-line best-line"></span>
      <span class="field-label best-label">BEST BEFORE</span>
    </div>
  </section>
</main>
</body>
</html>
```